MWR Snack Box for Printed Packaging

This is a BTL style 2 piece snack box. We have a jpeg logo and need it to be applied to the box along with some form of creative design. I have uploaded the keyline for the package. Please lay out the logo and design on this. Please bear in mind that the carton will be folded and appear like the photo which is also uploaded

Target Market(s)

General consumers in St. Lucia in the caribbean

Colors
EB3D1F
EC4F4E
F09395
F8D3D4
FCEDEE

```html
<!DOCTYPE html>
<html lang="en">
<head>
<meta charset="utf-8">
<title>MWR Snack Box – Keyline Layout</title>
<link rel="stylesheet" href="https://fonts.googleapis.com/css2?family=Barlow+Condensed:wght@600;700&display=swap">
<style>
  :root {
    --paper: #ffffff;
    --brand-red: #ee0000;
    --band-pink: #f06b6b;
    --mascot-tone: #f8d3d4;
    --keyline: #29abe2;
    --type-light: #ffffff;
  }
  html, body {
    margin: 0;
    width: 1200px;
    height: 500px;
    overflow: hidden;
    background: var(--paper);
  }
  .dieline-sheet {
    display: block;
    width: 1200px;
    height: 500px;
  }
  .band-check { fill: var(--band-pink); }
  .panel-red { fill: var(--brand-red); }
  .mascot-area { fill: var(--mascot-tone); }
  .brand-mark-dot { fill: var(--brand-red); }
  .brand-mark-name {
    font-family: "Barlow Condensed", sans-serif;
    font-weight: 700;
    fill: var(--brand-red);
  }
  .hero-name {
    font-family: "Barlow Condensed", sans-serif;
    font-weight: 700;
    fill: var(--type-light);
  }
  .keyline {
    fill: none;
    stroke: var(--keyline);
    stroke-width: 2;
    stroke-dasharray: 150 18;
  }
</style>
</head>
<body>
<svg class="dieline-sheet" viewBox="0 0 2560 1067" preserveAspectRatio="xMidYMid meet" xmlns="http://www.w3.org/2000/svg">
  <defs>
    <g id="box-unit">
      <!-- artwork on the front panel -->
      <rect class="band-check" x="291" y="349" width="639" height="48" role="img" aria-label="Red and white checkerboard band"/>
      <path class="panel-red" d="M620,397 H930 V648 H465 C600,630 650,560 645,485 C643,450 635,425 620,397 Z"/>
      <ellipse class="mascot-area" cx="405" cy="528" rx="45" ry="58" role="img" aria-label="Chef rooster mascot giving a thumbs up"/>
      <rect class="brand-mark-dot" x="445" y="505" width="16" height="16"/>
      <text class="brand-mark-name" x="468" y="520" font-size="34" textLength="86" lengthAdjust="spacingAndGlyphs">CRISPY</text>
      <text class="brand-mark-name" x="468" y="556" font-size="40" textLength="86" lengthAdjust="spacingAndGlyphs">BITE</text>
      <text class="hero-name" x="695" y="507" font-size="74" textLength="173" lengthAdjust="spacingAndGlyphs">CRISPY</text>
      <text class="hero-name" x="695" y="582" font-size="100" textLength="173" lengthAdjust="spacingAndGlyphs">BITE</text>

      <!-- keylines -->
      <path class="keyline" d="M291,203 L234,218 V338 L291,397"/>
      <path class="keyline" d="M291,400 H234 V590 L291,648"/>
      <path class="keyline" d="M291,203 V878 Q291,893 306,893 H596 Q611,893 611,878 V842 H905 Q927,842 927,820 V710 L907,672"/>
      <path class="keyline" d="M930,203 V648"/>
      <path class="keyline" d="M291,397 H1318 M291,648 H1318"/>
      <path class="keyline" d="M930,397 L1123,203 L1318,397"/>
      <path class="keyline" d="M930,648 L736,842"/>
      <path class="keyline" d="M930,648 L982,790 H1175 L1318,648"/>
      <path class="keyline" d="M1044,500 V540 Q1044,556 1060,556 H1188 Q1204,556 1204,540 V500 M1124,556 V600"/>
      <path class="keyline" d="M1318,397 V648"/>
    </g>
  </defs>

  <use href="#box-unit"/>
  <path class="keyline" d="M291,203 H1270 L1318,180"/>

  <use href="#box-unit" transform="translate(1027,0)"/>
  <path class="keyline" d="M1318,180 H1956 L2004,203 H2341 V648"/>
  <path class="keyline" d="M1318,180 V397"/>
</svg>
</body>
</html>
```